Company website design for Marlowfen Pricing Counsel LLC

Design of company website. See uploaded outline. Logo hex codes for the icon colors: middle blue - 4D6C8A, dark blue - 11122B.

```html
<!DOCTYPE html>
<html lang="en">
<head>
<meta charset="utf-8">
<title>Marlowfen Pricing Counsel LLC</title>
<link rel="stylesheet" href="https://fonts.googleapis.com/css2?family=Montserrat:wght@300;400;500;600;700&family=Open+Sans:wght@400;600&display=swap">
<style>
:root{
  --blue:#4D6C8A;
  --navy:#11122B;
  --band:#4f6e91;
  --footer:#1b1e30;
  --ink:#333845;
  --muted:#6d7280;
  --line:#c9ccd2;
  --soft:#f1f2f4;
  --white:#ffffff;
}
*{box-sizing:border-box;margin:0;padding:0}
html,body{width:1200px;height:4240px;overflow:hidden}
body{font-family:"Open Sans",Arial,sans-serif;color:var(--ink);background:var(--white);position:relative}
.heading{font-family:"Montserrat",Arial,sans-serif;font-weight:400;letter-spacing:2px;text-transform:uppercase;color:var(--ink)}
section,header,footer{position:absolute;left:0;width:1200px}

/* header */
.site-header{top:0;height:112px;background:var(--white);display:flex;align-items:center;padding:0 40px 0 108px;justify-content:space-between}
.brand{display:flex;align-items:center;gap:12px}
.brand-square{width:40px;height:40px;background:var(--navy)}
.brand-name{font-family:"Montserrat",Arial,sans-serif;font-weight:600;color:var(--navy);line-height:1.1;font-size:22px;letter-spacing:1px}
.brand-name small{display:block;font-size:10px;letter-spacing:1.6px;font-weight:600}
.main-nav{display:flex;gap:34px}
.main-nav a{font-family:"Montserrat",Arial,sans-serif;font-size:12px;font-weight:500;color:var(--ink);text-decoration:none;letter-spacing:.6px;text-align:center;display:flex;flex-direction:column;align-items:center;gap:8px}
.main-nav a::before{content:"";width:14px;height:14px;border:2px solid var(--blue);border-radius:50%}
.main-nav a.active{color:var(--blue)}

/* hero */
.hero{top:112px;height:688px}
.hero-photo{position:absolute;inset:0;background:linear-gradient(180deg,#c9d4df 0%,#9fb0c4 22%,#8a7e7c 40%,#6f5e52 55%,#b59761 72%,#8b6b3c 100%)}
.hero-title{position:absolute;top:180px;width:100%;text-align:center;color:var(--white);font-family:"Montserrat",Arial,sans-serif;font-weight:500;font-size:44px;line-height:62px;letter-spacing:3px;text-transform:uppercase;text-shadow:0 2px 8px rgba(0,0,0,.35)}
.hero-dots{position:absolute;top:572px;width:100%;display:flex;justify-content:center;gap:10px}
.hero-dots span{width:10px;height:10px;border-radius:50%;background:rgba(255,255,255,.55)}
.hero-dots span.on{background:var(--white)}

/* values */
.values{top:800px;height:568px}
.section-title{position:absolute;width:100%;text-align:center;font-size:34px}
.values .section-title{top:84px}
.values-chart{position:absolute;top:150px;left:0}

/* what we do */
.services{top:1368px;height:584px;background:var(--band);color:var(--white)}
.services-title{position:absolute;left:112px;top:118px;color:var(--white);font-size:30px;font-weight:500}
.services-title::after{content:"";position:absolute;left:0;top:50px;width:300px;height:2px;background:rgba(255,255,255,.7)}
.service{position:absolute;width:340px}
.service svg{display:block;margin-bottom:12px}
.service h3{font-family:"Montserrat",Arial,sans-serif;font-weight:600;font-size:18px;line-height:23px;text-transform:uppercase;letter-spacing:.6px;margin-bottom:10px}
.service p{font-size:13px;line-height:20px;color:#dfe6ee}

/* who we serve */
.audience{top:1952px;height:528px}
.audience .section-title{top:40px}
.audience-chart{position:absolute;top:100px;left:0}

/* industries */
.industries{top:2480px;height:840px;background:var(--soft)}
.industries-title{position:absolute;left:112px;top:74px;font-size:29px;letter-spacing:1.5px;white-space:nowrap}
.industries-intro{position:absolute;left:500px;top:64px;width:600px;font-size:13px;line-height:21px;color:var(--muted);padding-left:24px;border-left:2px solid var(--line)}
.industry{position:absolute;width:272px;height:272px;border-radius:50%;display:flex;align-items:center;justify-content:center;text-align:center;color:var(--white);font-family:"Montserrat",Arial,sans-serif;font-weight:600;font-size:17px;letter-spacing:1px;text-transform:uppercase;line-height:23px;text-shadow:0 1px 5px rgba(0,0,0,.5)}
.industry.featured{box-shadow:0 0 0 6px var(--blue)}

/* contact */
.contact{top:3320px;height:560px}
.contact .section-title{top:56px}
.contact-form{position:absolute;left:312px;top:124px;width:576px}
.field-row{display:flex;gap:16px;margin-bottom:16px}
.field{flex:1;height:50px;border:1px solid var(--line);padding:0 14px;display:flex;align-items:center;font-size:13px;color:#8a8f99}
.field.message{height:104px;align-items:flex-start;padding-top:14px}
.captcha{width:260px;height:56px;border:1px solid var(--line);background:#f9f9f9;display:flex;align-items:center;gap:12px;padding:0 12px;font-size:13px;color:var(--ink);margin-bottom:28px}
.captcha .box{width:22px;height:22px;border:2px solid #c1c1c1;background:var(--white)}
.captcha .badge{margin-left:auto;width:28px;height:28px;background:#c9d2de}
.submit{display:block;width:120px;height:40px;background:var(--blue);color:var(--white);font-family:"Montserrat",Arial,sans-serif;font-weight:600;font-size:13px;letter-spacing:1px;border:0;margin:0 auto}

/* footer */
.site-footer{top:3880px;height:360px;background:var(--footer);color:var(--white)}
.footer-brand{position:absolute;left:112px;top:100px}
.footer-brand .brand-square{background:var(--white)}
.footer-brand .brand-name{color:var(--white)}
.footer-block{position:absolute;display:flex;gap:14px}
.footer-block h4{font-family:"Montserrat",Arial,sans-serif;font-size:16px;font-weight:600;letter-spacing:1px;margin-bottom:6px}
.footer-block p{font-size:12px;line-height:18px;color:#c6cad3}
.socials{position:absolute;left:520px;top:160px;display:flex;gap:12px}
.socials span{width:30px;height:30px;border-radius:50%;border:2px solid var(--white)}
.footer-nav{position:absolute;top:222px;left:0;width:100%;border-top:1px solid rgba(255,255,255,.15);height:60px;display:flex;justify-content:center;align-items:center;gap:48px}
.footer-nav a{color:var(--white);text-decoration:none;font-family:"Montserrat",Arial,sans-serif;font-size:11px;font-weight:600;letter-spacing:.8px}
.copyright{position:absolute;top:296px;width:100%;text-align:center;font-size:12px;color:#c6cad3}
</style>
</head>
<body>

<header class="site-header">
  <div class="brand">
    <span class="brand-square"></span>
    <span class="brand-name">MARLOWFEN<small>PRICING COUNSEL LLC</small></span>
  </div>
  <nav class="main-nav">
    <a class="active" href="#">HOME</a>
    <a href="#">VALUES</a>
    <a href="#">WHAT WE DO</a>
    <a href="#">WHO WE SERVE</a>
    <a href="#">INDUSTRIES SERVED</a>
    <a href="#">CONTACT</a>
  </nav>
</header>

<section class="hero">
  <div class="hero-photo" role="img" aria-label="Mountain range at sunset above a golden meadow and a highway leading toward the peaks"></div>
  <h1 class="hero-title">We have the valuation expertise<br>to guide you</h1>
  <div class="hero-dots"><span class="on"></span><span></span><span></span></div>
</section>

<section class="values">
  <h2 class="heading section-title">Our Values</h2>
  <svg class="values-chart" width="1200" height="400" viewBox="0 0 1200 400" font-family="Montserrat, Arial, sans-serif">
    <g fill="none" stroke="#c4c8ce" stroke-width="3">
      <path d="M318 182 l26 26 m0 -16 v16 h-16"/>
      <path d="M478 182 l26 -26 m-16 0 h16 v16"/>
      <path d="M678 182 l26 26 m0 -16 v16 h-16"/>
      <path d="M838 182 l26 -26 m-16 0 h16 v16"/>
    </g>
    <g fill="#fff" stroke="#c9ccd2" stroke-width="2">
      <rect x="-72" y="-72" width="144" height="144" rx="18" transform="translate(240 140) rotate(45)"/>
      <rect x="-72" y="-72" width="144" height="144" rx="18" transform="translate(420 240) rotate(45)"/>
      <rect x="-72" y="-72" width="144" height="144" rx="18" transform="translate(600 140) rotate(45)"/>
      <rect x="-72" y="-72" width="144" height="144" rx="18" transform="translate(780 240) rotate(45)"/>
      <rect x="-72" y="-72" width="144" height="144" rx="18" transform="translate(960 140) rotate(45)" stroke="#4a4f5c" stroke-width="3"/>
    </g>
    <g fill="none" stroke="#9aa0a9" stroke-width="2">
      <circle cx="240" cy="112" r="10"/><path d="M226 134 q14 -14 28 0"/>
      <path d="M408 214 h24 v18 h-24z M414 214 v-6 h12 v6"/>
      <path d="M600 96 l6 12 13 2 -9 9 2 13 -12 -6 -12 6 2 -13 -9 -9 13 -2z"/>
      <path d="M764 226 l10 -8 12 8 12 -8 10 8 -12 12 -10 -6 -10 6z"/>
      <circle cx="960" cy="112" r="16" stroke="#4a4f5c"/><circle cx="960" cy="112" r="6" stroke="#4a4f5c"/>
    </g>
    <g font-size="13" letter-spacing="1.5" fill="#9aa0a9" text-anchor="middle">
      <text x="240" y="160">INTEGRITY</text>
      <text x="420" y="262">RESPONSIVENESS</text>
      <text x="600" y="160">EXCELLENCE</text>
      <text x="780" y="262">RELATIONSHIPS</text>
      <text x="960" y="160" fill="#3a3f4b" font-weight="600">COMMUNITY</text>
    </g>
  </svg>
</section>

<section class="services">
  <h2 class="heading services-title">What We Do</h2>

  <article class="service" style="left:440px;top:90px">
    <svg width="40" height="40" viewBox="0 0 40 40" fill="none" stroke="#fff" stroke-width="2"><rect x="6" y="4" width="24" height="32" rx="2"/><path d="M12 14h12M12 20h12M12 26h8"/><circle cx="31" cy="30" r="6"/></svg>
    <h3>Tax-Related Valuations</h3>
    <p>Valuations for estate and gift tax, charitable giving, equity-based compensation, corporate restructuring and ownership transfers.</p>
  </article>

  <article class="service" style="left:800px;top:90px">
    <svg width="40" height="40" viewBox="0 0 40 40" fill="none" stroke="#fff" stroke-width="2"><path d="M4 36h32M8 30v-8M16 30v-14M24 30v-10M32 30v-20"/><path d="M8 16l8 -6 8 4 8 -8"/></svg>
    <h3>Financial Reporting</h3>
    <p>Fair value work for purchase price allocations, goodwill impairment testing, equity compensation and complex financial instruments.</p>
  </article>

  <article class="service" style="left:440px;top:320px">
    <svg width="40" height="40" viewBox="0 0 40 40" fill="none" stroke="#fff" stroke-width="2"><rect x="4" y="10" width="28" height="20" rx="2"/><path d="M4 16h28M10 24h8"/><circle cx="32" cy="30" r="6"/></svg>
    <h3>Financing &amp; Transaction<br>Advisory</h3>
    <p>Objective analysis to support capital structure decisions, fairness opinions, solvency reviews, buy-sell agreements, mergers and acquisitions.</p>
  </article>

  <article class="service" style="left:800px;top:320px">
    <svg width="40" height="40" viewBox="0 0 40 40" fill="none" stroke="#fff" stroke-width="2"><rect x="4" y="6" width="32" height="22" rx="2"/><path d="M20 28v6M12 36h16M10 22l7 -7 5 4 8 -8"/></svg>
    <h3>Business Planning &amp;<br>Advisory</h3>
    <p>Independent guidance on ownership transitions, succession planning, strategic alternatives and long-term value growth.</p>
  </article>
</section>

<section class="audience">
  <h2 class="heading section-title">Who Do We Serve</h2>
  <svg class="audience-chart" width="1200" height="420" viewBox="0 0 1200 420" font-family="Montserrat, Arial, sans-serif">
    <circle cx="600" cy="210" r="180" fill="none" stroke="#3f4656" stroke-width="3"/>
    <rect x="545" y="155" width="110" height="110" fill="#11122B"/>
    <text x="600" y="215" text-anchor="middle" fill="#fff" font-size="12" font-weight="600" letter-spacing="1">MARLOWFEN</text>
    <g fill="#fff" stroke="#3f4656" stroke-width="3">
      <circle cx="473" cy="83" r="42"/><circle cx="727" cy="83" r="42"/>
      <circle cx="473" cy="337" r="42"/><circle cx="727" cy="337" r="42"/>
    </g>
    <g fill="none" stroke="#4D6C8A" stroke-width="2.5">
      <circle cx="463" cy="76" r="7"/><circle cx="483" cy="76" r="7"/><path d="M451 100q12 -14 24 0M471 100q12 -14 24 0"/>
      <path d="M711 102v-30h14v30M725 102v-22h16v22M706 102h40M716 80h4M716 88h4"/>
      <path d="M459 352v-12M469 352v-22M479 352v-16M489 352v-28M453 354h42"/>
      <path d="M709 330l18 -12 18 12zM713 334v16M722 334v16M732 334v16M741 334v16M707 352h40"/>
    </g>
    <g font-size="14" font-weight="600" fill="#2c303b" letter-spacing=".5">
      <text x="404" y="78" text-anchor="end">CLOSELY-HELD / FAMILY</text>
      <text x="404" y="98" text-anchor="end">OWNED BUSINESSES</text>
      <text x="796" y="78">PRIVATE-EQUITY</text>
      <text x="796" y="98">SPONSORED COMPANIES</text>
      <text x="404" y="330" text-anchor="end">PUBLICLY TRADED</text>
      <text x="404" y="350" text-anchor="end">COMPANIES</text>
      <text x="796" y="342">LENDERS</text>
    </g>
  </svg>
</section>

<section class="industries">
  <h2 class="heading industries-title">Industries Served</h2>
  <p class="industries-intro">We bring deep sector knowledge to every engagement, pairing rigorous analysis with a clear understanding of the forces that shape value in each market we serve.</p>

  <div class="industry featured" style="left:164px;top:204px;background:radial-gradient(circle at 40% 40%,#2d4e7c,#101a33)" role="img" aria-label="Night city skyline with glowing network lines">Technology</div>
  <div class="industry" style="left:464px;top:204px;background:radial-gradient(circle at 50% 45%,#8aa0b8,#4b5d73)" role="img" aria-label="Gloved hands working on machine parts">Manufacturing</div>
  <div class="industry" style="left:792px;top:204px;background:radial-gradient(circle at 50% 50%,#c8b9a3,#7d6c5a)" role="img" aria-label="Warehouse aisles stacked with shelves of goods">Wholesale<br>Distribution</div>
  <div class="industry" style="left:164px;top:504px;background:radial-gradient(circle at 50% 40%,#4f5f7e,#1f2840)" role="img" aria-label="Modern office building exterior">Business &amp;<br>Professional Services</div>
  <div class="industry" style="left:464px;top:504px;background:radial-gradient(circle at 50% 50%,#b16f5b,#5d3a34)" role="img" aria-label="Shopping bags in a retail store">Retail</div>
  <div class="industry" style="left:792px;top:504px;background:radial-gradient(circle at 50% 50%,#e0a05c,#9a5d3a)" role="img" aria-label="Colourful packaged consumer goods">Consumer Products</div>
</section>

<section class="contact">
  <h2 class="heading section-title">Contact Us</h2>
  <form class="contact-form">
    <div class="field-row"><div class="field">First Name</div><div class="field">Last Name</div></div>
    <div class="field-row"><div class="field">Email</div><div class="field">Phone</div></div>
    <div class="field-row"><div class="field message">Message</div></div>
    <div class="captcha"><span class="box"></span>I'm not a robot<span class="badge"></span></div>
    <button class="submit" type="button">SUBMIT</button>
  </form>
</section>

<footer class="site-footer">
  <div class="brand footer-brand">
    <span class="brand-square"></span>
    <span class="brand-name">MARLOWFEN<small>PRICING COUNSEL LLC</small></span>
  </div>

  <div class="footer-block" style="left:480px;top:70px">
    <svg width="22" height="28" viewBox="0 0 22 28" fill="none" stroke="#fff" stroke-width="2"><path d="M11 26s9-9 9-15a9 9 0 0 0-18 0c0 6 9 15 9 15z"/><circle cx="11" cy="11" r="3"/></svg>
    <div>
      <h4>ADDRESS</h4>
      <p>418 W Harlan Crest Rd<br>Suite 12, Brenwick, ID 83700</p>
    </div>
  </div>
  <div class="socials"><span></span><span></span></div>

  <div class="footer-block" style="left:820px;top:70px">
    <svg width="22" height="22" viewBox="0 0 22 22" fill="none" stroke="#fff" stroke-width="2"><path d="M5 2h4l2 5-3 2a12 12 0 0 0 5 5l2-3 5 2v4a2 2 0 0 1-2 2A17 17 0 0 1 3 4a2 2 0 0 1 2-2z"/></svg>
    <div><h4>PHONE</h4><p>+1 555-014-2290</p></div>
  </div>
  <div class="footer-block" style="left:820px;top:140px">
    <svg width="22" height="18" viewBox="0 0 22 18" fill="none" stroke="#fff" stroke-width="2"><rect x="1" y="1" width="20" height="16" rx="2"/><path d="M1 3l10 7 10-7"/></svg>
    <div><h4>EMAIL</h4><p>hello@marlowfenpricing.example</p></div>
  </div>

  <nav class="footer-nav">
    <a href="#">HOME</a><a href="#">VALUES</a><a href="#">WHAT WE DO</a><a href="#">WHO WE SERVE</a><a href="#">INDUSTRIES SERVED</a><a href="#">CONTACT US</a>
  </nav>
  <p class="copyright">Marlowfen Pricing © 2023 All Rights Reserved.</p>
</footer>

</body>
</html>
```